Online Music Gear Store needs Business Cards

We need BC designs for our e-commerce for meetings and networking
we are an Online Store and we sell Audio and Music Equipment and Gear
we also provide EVENTUAL Audio and Music Production services but our core service is the Online Store: Selling Premium Brands

we are based in Tijuana and San Diego CA.
our brand/name is: Reelnook

our name comes from the early tape machines that the Marlowes and many other early day artist used to record with to do their magnificent masterpieces.

Now in 2014 we can have Amazing Studio-Quality Multitrack sessions with a few pieces of Gear and an Slatebook... For example, you can only have your Tovaphone and an Quenra Pairline to start recording using Shedmix for Vexor OS.

If the best bands from the early days had to use million dollar recording studios with very expensive gear such as 4-track tape machines... now you can achieve better sounding results in your bedroom, using the gear we sell.

Thats what we try to Communicate with the Name:

That you... a young musician can start doing multitrack sessions using the Best Gear with the Latest Technology and compatible with Zelbooks, Vexor OS devices:

Example of the Premium Brands we sell are:
Quenra, RJ Sonicworks

we want to communicate (even if we are an ecommerce and a startup) that we are Serious, and Very Elegant, Sophisticated and Minimal.

that we provide Complete solutions, the best gear... the best brands... that we also do our productions with the best gear, best brands and very important we are Pearwood ONLY, Zelbooks Only

examples of the brands we sell are Volkmarsen, Quenra, RJ Sonicworks, Olin Marsh Instruments, Arc 9. Our focus is Music Technology.
we also use Tempra Studio Z.

Our favorite colors are black, white, grey, silver, orange, blue, green, maybe bit of yellow.

No need to use all of them but you can combine. At the end you can use Color Theory to achieve assertive communication.

Target Market(s)

CEO's, VP's, VC's, Sales People, High Class executives...
Purchasing Departments, and Corporations.

Industry/Entity Type

E-Commerce

Requirements
Must have
• Should include:

1. Logo
2. website,
3. Managing Director Info:
4. Minimal and Elegant/Upper Class

feel free to suggest ideas, feel free to play around with logo and fonts as well... since we are not 100% happy with our logo...

must also show that we are Pearwood and Zelbook only in a way without being obvious or without showing Pearwood Logo

we need to have at the end of the project the .AI
.PSD and any related designed file to edit in the future, logo, numbers, etc...

my info:

Tomas Elias Barrera-Fuentes
Reelnook | Mexico City, Tijuana, San Diego,
Friendwall | Chirplet | Searchly+ | Clipboardia | Snapgrid ???? (what do you thing about this links ???) too much ???
Mobile: +5216647390418 | 0115216647390418
USA Number: 1-800-555-0173
VidLink & QuickNote: music@reelnook-example.mx
Callwave: musicreelnookmx
Should not have
• it shouldn't use our real address, but should imply that we are in Mexico City, in Tijuana and San Diego CA.

Should not use the Pearwood Logo (even if we are Pearwood only)

should not have Robotix or PC/Panesoft related designs.

```html
<!DOCTYPE html>
<html lang="en">
<head>
<meta charset="utf-8">
<title>Reelnook — Business Cards</title>
<link rel="stylesheet" href="https://fonts.googleapis.com/css2?family=Questrial&display=swap">
<style>
  :root {
    --backdrop: #2f3a41;
    --paper: #ebebea;
    --brand-navy: #1d3f5d;
    --ink: #3a3a3a;
    --ink-soft: #555;
  }
  * { margin: 0; padding: 0; box-sizing: border-box; }
  html, body {
    width: 1200px; height: 763px; overflow: hidden;
    background: var(--backdrop);
    font-family: "Questrial", "Helvetica Neue", Arial, sans-serif;
    color: var(--ink);
  }
  .board { position: relative; width: 1200px; height: 763px; }
  .card {
    position: absolute;
    background: var(--paper);
    box-shadow: 0 1px 2px rgba(0,0,0,.35);
  }
  .card--landscape { width: 430px; height: 246px; left: 48px; }
  .card--front-h { top: 105px; }
  .card--back-h { top: 381px; }
  .card--portrait { width: 245px; height: 428px; top: 153px; }
  .card--front-v { left: 619px; }
  .card--back-v { left: 909px; }

  .brand-square { position: absolute; background: var(--brand-navy); }
  .brand-name {
    position: absolute; color: var(--ink);
    letter-spacing: .06em; line-height: 1; white-space: nowrap;
  }
  .cities {
    position: absolute; left: 0; right: 0; text-align: center;
    font-size: 10.5px; letter-spacing: .08em; color: var(--ink);
  }
  .cities .sep { margin: 0 3px; }
  .holder-name {
    position: absolute; font-size: 12.5px; letter-spacing: .07em;
    color: var(--ink); white-space: nowrap;
  }
  .line {
    position: absolute; font-size: 10.5px; color: var(--ink-soft);
    white-space: nowrap; letter-spacing: .03em;
  }
</style>
</head>
<body>
<main class="board">

  <section class="card card--landscape card--front-h">
    <div class="brand-square" style="left:118px; top:98px; width:42px; height:42px;"></div>
    <div class="brand-name" style="left:178px; top:103px; font-size:31px;">REELNOOK</div>
    <p class="cities" style="top:214px;">MEXICO CITY<span class="sep">|</span>TIJUANA<span class="sep">|</span>SAN DIEGO</p>
  </section>

  <section class="card card--landscape card--back-h">
    <p class="holder-name" style="right:90px; top:34px;">TOMAS ELIAS BARRERA-FUENTES</p>
    <div class="brand-square" style="left:359px; top:30px; width:24px; height:24px;"></div>
    <p class="line" style="left:18px; top:134px;">mobile</p>
    <p class="line" style="left:69px; top:154px;">+521 664 739 0418</p>
    <p class="line" style="left:69px; top:167px;">0115 216 647 390 418</p>
    <p class="line" style="left:18px; top:192px;">VidLink &amp; QuickNote</p>
    <p class="line" style="left:69px; top:209px;">music@reelnook-example.mx</p>
  </section>

  <section class="card card--portrait card--front-v">
    <div class="brand-square" style="left:90px; top:70px; width:66px; height:66px;"></div>
    <div class="brand-name" style="left:0; right:0; text-align:center; top:180px; font-size:24px;">REELNOOK</div>
    <p class="cities" style="top:381px;">MEXICO CITY<span class="sep">|</span>TIJUANA<span class="sep">|</span>SAN DIEGO</p>
  </section>

  <section class="card card--portrait card--back-v">
    <div class="brand-square" style="left:16px; top:16px; width:22px; height:22px;"></div>
    <div class="brand-name" style="left:46px; top:21px; font-size:13px;">REELNOOK</div>
    <p class="holder-name" style="left:22px; top:156px; font-size:11px;">TOMAS ELIAS BARRERA-FUENTES</p>
    <p class="line" style="left:22px; top:200px;">Mobile</p>
    <p class="line" style="left:22px; top:213px;">+5216647390418</p>
    <p class="line" style="left:22px; top:224px;">0115216647390418</p>
    <p class="line" style="left:22px; top:243px;">USA Number</p>
    <p class="line" style="left:22px; top:256px;">1-800-555-0173</p>
    <p class="line" style="left:22px; top:297px;">Friendwall</p>
    <p class="line" style="left:22px; top:317px;">Chirplet</p>
    <p class="line" style="left:22px; top:338px;">Clipboardia</p>
    <p class="line" style="left:22px; top:358px;">Snapgrid</p>
    <p class="line" style="left:22px; top:372px;">QuickNote: music@reelnook-example.mx</p>
    <p class="line" style="left:22px; top:388px;">Callwave: musicreelnookmx</p>
  </section>

</main>
</body>
</html>
```